Doctors Office Web Design

Name of the business is Lian-Hua Qiu M.D.
We need a web design that is attractive for women that want to see Dr. Lian-Hua Qiu for Obstetrician Gynecology and Pregnancy care. Dr. Qiu earned her degree from Harbor Crest Medical College of obstetrician gynecology. We want to attract women of child bearing ages to come to our offices for health, education, and pregnancies.

Please visit http://www.drqiucare-example.com/ to help you get a feel for who we are. We will be adding some pictures and logo in the next few days.

We are looking for to have pages for and tabs including
About Us- History, Our Staff, Dr. Qiu
Patient Information- Appointments, E-Prescriptions, Payments Accepted, Insurance
Health- General, Sexual, Mental, Affiliates
Pregnancy- Minimally invasive surgery(our specialty), 4-D Ultra Sound, Hospital Affiliations
Media- News,Pictures, Videos
Locations- Palmvale Office, Marlow Office

The colors we would like to use are pastel colors, magenta, and plum

Target Market(s)

Women of all ages with an emphasis on 25-65 year olds

Industry/Entity Type

Business

Requirements
Must have
• Needs to include a location for a our videos and pictures that I will submit shortly. We also want a map to our location or atleast a place for one.
Nice to have
• A place for a google map of our office locations.

```html
<!DOCTYPE html>
<html lang="en">
<head>
<meta charset="utf-8">
<title>Dr. Qiu's website</title>
<link rel="stylesheet" href="https://fonts.googleapis.com/css2?family=Anton&family=Arimo:wght@400;700&display=swap">
<style>
:root{
  --page-bg:#2a1e1d;
  --plum:#5b1256;
  --plum-text:#86157f;
  --mauve-top:#a56aa8;
  --mauve-mid:#c99bcc;
  --blush:#efe0f0;
  --ink:#111;
  --link:#6a1470;
  --tab-top:#ffffff;
  --tab-bottom:#ead6ec;
  --box-border:#b172b4;
  --video-blue:#1a7fb8;
}
*{margin:0;padding:0;box-sizing:border-box}
html,body{width:1200px;height:1043px;overflow:hidden;background:var(--page-bg)}
body{font-family:"Arimo",Arial,sans-serif;color:var(--ink)}
.stage{position:absolute;left:0;top:0;width:1150px;height:1000px;transform:scale(1.04348);transform-origin:0 0}
.sheet{position:absolute;left:84px;top:30px;width:990px;height:925px;border-radius:12px;
  background:linear-gradient(180deg,var(--mauve-top) 0%,#b47bb6 30%,var(--mauve-mid) 55%,var(--blush) 75%,#fbf6fb 97%,#fff 97.1%);overflow:hidden}
.abs{position:absolute}
.site-title{left:145px;top:40px;font-family:"Anton",sans-serif;font-size:51px;color:#fff;letter-spacing:.3px;text-shadow:2px 3px 3px rgba(60,10,60,.55)}
.doctor{left:800px;top:75px;width:240px;text-align:center;color:#fff}
.doctor-name{font-size:21px;letter-spacing:.3px}
.doctor-sub{font-size:14px;line-height:17px;margin-top:3px}
.tabs{left:139px;top:116px;display:flex;list-style:none}
.tab{height:34px;margin-right:3px;border-radius:7px 7px 0 0;background:linear-gradient(180deg,var(--tab-top),var(--tab-bottom));
  font-size:15px;display:flex;align-items:center;justify-content:center}
.tab.active{background:linear-gradient(180deg,#f4f4f4,#d9d9db)}
.hero-frame{left:139px;top:150px;width:894px;height:316px;background:var(--plum);border-radius:10px}
.hero-photo{left:146px;top:157px;width:879px;height:303px;border-radius:6px;
  background:linear-gradient(90deg,#e9dcd6 0%,#f6eee9 30%,#f3f1f2 55%,#e2e3e6 75%,#d7c3bf 100%)}
.intro{left:148px;top:482px;width:592px;font-size:14px;line-height:18px}
.intro a,.contact a{color:var(--link)}
.services{left:148px;top:568px;width:560px}
.services h2{font-size:15px;font-weight:700}
.services p{font-size:15px;line-height:19px}
.explore{left:148px;top:646px;width:600px}
.explore h2{font-size:16px;font-weight:700}
.contact{font-size:13px}
.map{left:769px;top:472px;width:271px;height:212px;border-radius:8px;border:2px solid #c9a4cc;
  background:linear-gradient(135deg,#e8e4dc,#efe9dd 50%,#e4dfd4)}
.badge{left:108px;top:755px;width:96px;height:135px}
.office{width:244px;height:189px;border:3px solid var(--box-border);border-radius:8px;
  background:linear-gradient(160deg,#f4d7f4,#e2b3e3 50%,#f0d2f0);text-align:center;font-size:15px;line-height:23px}
.office h3{font-family:"Anton",sans-serif;font-weight:400;font-size:32px;color:var(--plum-text);text-align:left;padding-left:9px;line-height:42px;
  text-shadow:1px 1px 1px rgba(255,255,255,.6)}
.video{left:770px;top:707px;width:271px;height:189px;border-radius:5px;background:linear-gradient(180deg,#2b9fd6,var(--video-blue))}
.footer-links{left:84px;top:930px;width:990px;text-align:center;font-size:12px;color:#111}
.copyright{left:0;top:965px;width:1150px;text-align:center;font-size:11px;color:#fff}
</style>
</head>
<body>
<div class="stage">
  <div class="sheet"></div>

  <h1 class="abs site-title">Dr. qiu's website</h1>
  <div class="abs doctor">
    <div class="doctor-name">LIAN-HUA QIU, M.D.</div>
    <div class="doctor-sub">facog board certified<br>Obstetrician/Gynecologist</div>
  </div>

  <ul class="abs tabs">
    <li class="tab active" style="width:89px">Home</li>
    <li class="tab" style="width:90px">About Us</li>
    <li class="tab" style="width:139px">Patient Information</li>
    <li class="tab" style="width:90px">Health</li>
    <li class="tab" style="width:139px">PregnancyMedia</li>
    <li class="tab" style="width:100px">Locations</li>
  </ul>

  <div class="abs hero-frame"></div>
  <div class="abs hero-photo" role="img" aria-label="Photo of a mother holding a smiling baby and a doctor examining an infant with its mother"></div>

  <p class="abs intro">Welcome to <b>Dr. Lian-Hua Qiu's website</b>. Here you will be able to find information about both of our offices, meet Dr. Qiu and her staff, and browse through our women's health links to learn more about pregnancy, nutrition, exercise, and other women's health issues. Have fun and if you have any questions, feel free to contact us at <a href="#">drqiu@careletter-mail.net</a></p>

  <div class="abs services">
    <h2>Serving All Areas of Women's Health, including:</h2>
    <p>Obstetrics, Family Planning, Hormonal Evaluation, Incontinence, Infertility, and Gynecology Surgery</p>
  </div>

  <div class="abs explore">
    <h2>Start exploring Dr. Qiu's Site</h2>
    <p class="contact">Contact us!&nbsp; Send e-mail to <a href="#">drqiu@careletter-mail.net</a> with your comments and suggestions for this site.</p>
  </div>

  <div class="abs map" role="img" aria-label="Street map showing the office location"></div>

  <svg class="abs badge" viewBox="0 0 96 135" role="img" aria-label="Awareness month badge">
    <ellipse cx="48" cy="38" rx="26" ry="37" fill="#4b2a6a"/>
    <rect x="8" y="92" width="80" height="18" fill="#4b2a6a" opacity=".5"/>
    <rect x="4" y="118" width="88" height="10" fill="#4b2a6a" opacity=".3"/>
  </svg>

  <div class="abs office" style="left:234px;top:708px">
    <h3>Our Office</h3>
    <p style="margin-top:4px">2480 Seagrove Avenue<br>Suite 210-212<br>Marlow Beach, Florida&nbsp; 30415<br>Tel:&nbsp; (555) 014-4545<br>Fax:&nbsp; (555) 014-0528</p>
  </div>
  <div class="abs office" style="left:503px;top:708px">
    <h3>Our Office</h3>
    <p style="margin-top:-10px;line-height:25px">760 N.W. 22nd Street<br>Suite 140B<br>Palmvale, Florida&nbsp; 30487<br>Tel:&nbsp; (555) 019-4014<br>Fax:&nbsp; (555) 019-2753</p>
  </div>

  <div class="abs video">
    <svg width="271" height="189" viewBox="0 0 271 189" role="img" aria-label="Video player">
      <rect x="7" y="6" width="258" height="160" fill="#000"/>
      <rect x="113" y="71" width="46" height="31" rx="6" fill="#9a9a9a"/>
      <path d="M130 79 L145 86.5 L130 94 Z" fill="#fff"/>
      <text x="258" y="158" text-anchor="end" font-family="Arimo, sans-serif" font-size="10" fill="#bbb">ClipHost</text>
      <rect x="7" y="166" width="258" height="17" fill="#dfe9f1"/>
      <path d="M12 170 L19 174.5 L12 179 Z" fill="#234"/>
      <rect x="28" y="172" width="128" height="5" rx="2.5" fill="#8aa2b4"/>
      <circle cx="31" cy="174.5" r="4" fill="#556"/>
      <text x="166" y="178" font-family="Arimo, sans-serif" font-size="7" fill="#234">0:00 / 0:00</text>
      <rect x="205" y="170" width="12" height="9" fill="#345"/>
      <rect x="225" y="170" width="14" height="9" fill="#345"/>
      <rect x="245" y="170" width="14" height="9" fill="#345"/>
    </svg>
  </div>

  <nav class="abs footer-links">Home | About Us | Patient Information | Health | Pregnancy&nbsp; Media | Locations</nav>
  <p class="abs copyright">(c) Copyright 2002, Lian-Hua Qiu, M.D., P.A.</p>
</div>
</body>
</html>
```